I Need a Banner for Web Advertising

impression banner for brivola AD
size 728x90, 320x50 , 160x600 , 300x600 , 100x50
Banner background bright blue
would like the AD to say -
We pay cash for houses in any condition
Probate,foreclosure, Pass due property taxes ect
470-555-0193
Updates
We would like to change the words to -
We pay cash for houses in any condition!
Probate, Foreclosure, Pass Due Property Taxes, and more!
470-555-0193
Target Market(s)
consumers that need to sale
Industry/Entity Type
Real Estate

```html
<!DOCTYPE html>
<html lang="en">
<head>
<meta charset="utf-8">
<title>Brivola Web Banners</title>
<link href="https://fonts.googleapis.com/css2?family=Lato:wght@700;900&family=Montserrat:wght@700&display=swap" rel="stylesheet">
<style>
  :root {
    --sky: #23a8cf;
    --sky-deep: #1c95bd;
    --orange: #f7941d;
    --yellow: #f9b21b;
    --white: #ffffff;
    --ink: #161616;
    --sheet: #e6e6e6;
    --sheet-edge: #cfcfcf;
    --shadow: 3px 3px 5px rgba(0,0,0,.35);
  }
  * { margin: 0; padding: 0; box-sizing: border-box; }
  html, body { width: 1200px; height: 895px; overflow: hidden; }
  body {
    position: relative;
    background: radial-gradient(ellipse at 50% 45%, #f1f1f1 0%, var(--sheet) 60%, var(--sheet-edge) 100%);
    font-family: "Lato", sans-serif;
    font-weight: 700;
    color: var(--white);
  }
  .banner {
    position: absolute;
    overflow: hidden;
    background: linear-gradient(135deg, var(--sky) 0%, var(--sky-deep) 100%);
    box-shadow: var(--shadow);
  }
  .accent { color: var(--yellow); }
  .tag {
    position: absolute;
    background: var(--orange);
    color: var(--white);
    line-height: 1.05;
    white-space: nowrap;
  }
  .photo {
    position: absolute;
    background: linear-gradient(180deg, rgba(35,168,207,0) 0%, #6f5a45 40%, #4c3b2c 62%, #7f8a3a 80%, #9aa042 100%);
  }
  .brand {
    font-family: "Lato", sans-serif;
    font-weight: 900;
    color: var(--ink);
    letter-spacing: .5px;
    text-transform: uppercase;
    white-space: nowrap;
  }
  .phone {
    font-family: "Montserrat", sans-serif;
    font-weight: 700;
    color: var(--white);
    white-space: nowrap;
  }

  /* 728x90 leaderboard */
  .leaderboard { left: 120px; top: 73px; width: 674px; height: 83px; }
  .leaderboard .logo-panel { position: absolute; left: 0; top: 0; }
  .leaderboard .brand { position: absolute; left: 0; top: 12px; width: 140px; text-align: center; font-size: 19px; }
  .leaderboard .phone-box { position: absolute; left: 0; top: 47px; width: 125px; height: 36px; background: var(--orange); }
  .leaderboard .phone { position: absolute; left: 0; top: 9px; width: 125px; text-align: center; font-size: 15px; font-family: "Lato", sans-serif; }
  .leaderboard .headline { position: absolute; left: 139px; top: 17px; font-size: 21px; line-height: 30px; }
  .leaderboard .headline .l1 { padding-left: 25px; display: block; }
  .leaderboard .tag { font-size: 14px; padding: 3px 6px; height: 21px; }
  .leaderboard .photo { left: 566px; top: 0; width: 108px; height: 83px; }

  /* 100x50 */
  .mini { left: 873px; top: 92px; width: 93px; height: 46px; }
  .mini p { position: absolute; left: 0; top: 4px; width: 93px; text-align: center; font-size: 10.5px; line-height: 12px; }
  .mini-logo { position: absolute; left: 995px; top: 92px; width: 93px; height: 46px; background: var(--white); box-shadow: var(--shadow); }
  .mini-logo .brand { position: absolute; left: 0; top: 16px; width: 93px; text-align: center; font-size: 12px; }

  /* 300x600 */
  .skyscraper-wide { left: 120px; top: 196px; width: 278px; height: 557px; }
  .skyscraper-wide .headline { position: absolute; left: 55px; top: 34px; font-size: 28px; line-height: 34px; }
  .skyscraper-wide .tag { left: 0; height: 26px; padding: 4px 0 0 55px; font-size: 17.5px; }
  .skyscraper-wide .photo { left: 0; top: 296px; width: 278px; height: 190px; }
  .skyscraper-wide .brand { position: absolute; left: 0; top: 474px; width: 278px; text-align: center; font-size: 30px; }
  .skyscraper-wide .phone-band { position: absolute; left: 0; top: 521px; width: 278px; height: 36px; background: var(--orange); }
  .skyscraper-wide .phone { display: block; text-align: center; font-size: 22px; letter-spacing: 3px; line-height: 36px; }

  /* 160x600 */
  .skyscraper { left: 433px; top: 196px; width: 150px; height: 557px; }
  .skyscraper .headline { position: absolute; left: 12px; top: 28px; font-size: 21px; line-height: 25px; }
  .skyscraper .tag { left: 0; padding: 4px 0 0 38px; font-size: 19px; white-space: normal; line-height: 19px; }
  .skyscraper .photo { left: 0; top: 345px; width: 150px; height: 150px; }
  .skyscraper .brand { position: absolute; left: 0; top: 500px; width: 150px; text-align: center; font-size: 18px; }
  .skyscraper .phone-band { position: absolute; left: 0; top: 531px; width: 150px; height: 26px; background: var(--orange); }
  .skyscraper .phone { display: block; text-align: center; font-size: 17px; line-height: 26px; font-family: "Lato", sans-serif; }

  /* 320x50 set */
  .strip { left: 612px; width: 324px; height: 46px; }
  .strip .photo { left: 255px; top: 0; width: 69px; height: 46px; }
  .strip .headline { position: absolute; left: 0; top: 2px; width: 290px; text-align: center; font-size: 19.5px; line-height: 20px; }
  .strip .tag { top: 13px; height: 23px; text-align: center; font-size: 16.5px; padding-top: 3px; }
  .strip-logo { position: absolute; left: 612px; top: 472px; width: 324px; height: 46px; background: var(--white); box-shadow: var(--shadow); }
  .strip-logo .brand { display: block; text-align: center; font-size: 29px; line-height: 46px; }
  .strip-phone { position: absolute; left: 615px; top: 542px; width: 321px; height: 46px; background: var(--orange); box-shadow: var(--shadow); }
  .strip-phone .phone { display: block; text-align: center; font-size: 23px; letter-spacing: 3.5px; line-height: 46px; }
</style>
</head>
<body>

  <!-- 728x90 -->
  <section class="banner leaderboard">
    <div class="photo" role="img" aria-label="Photo of an old weathered wooden farmhouse"></div>
    <svg class="logo-panel" width="151" height="47" viewBox="0 0 151 47"><polygon points="0,0 151,0 125,47 0,47" fill="#ffffff"/></svg>
    <span class="brand">Brivola</span>
    <div class="phone-box"><span class="phone">470-555-0193</span></div>
    <p class="headline"><span class="l1">We paid cost for</span>houses <span class="accent">in any condition</span></p>
    <span class="tag" style="left:361px;top:17px;">Probate</span>
    <span class="tag" style="left:433px;top:17px;">Facing for Closure</span>
    <span class="tag" style="left:361px;top:47px;">Pass due property taxes</span>
    <span class="tag" style="left:541px;top:47px;">etc...</span>
  </section>

  <!-- 100x50 -->
  <section class="banner mini">
    <p>We paid cash for houses <span class="accent">in any condition</span></p>
  </section>
  <div class="mini-logo"><span class="brand">Brivola</span></div>

  <!-- 300x600 -->
  <section class="banner skyscraper-wide">
    <p class="headline">We pay cash<br>for houses <span class="accent">in</span><br><span class="accent">any condition!</span></p>
    <span class="tag" style="top:156px;width:152px;">Probate,</span>
    <span class="tag" style="top:194px;width:202px;">Facing for Closure</span>
    <span class="tag" style="top:230px;width:250px;">Pass due property taxes</span>
    <span class="tag" style="top:266px;width:141px;">and more!</span>
    <div class="photo" role="img" aria-label="Photo of an old weathered wooden farmhouse on a grassy field"></div>
    <svg style="position:absolute;left:0;top:449px" width="278" height="72" viewBox="0 0 278 72"><polygon points="0,26 139,0 278,26 278,72 0,72" fill="#ffffff"/></svg>
    <span class="brand">Brivola</span>
    <div class="phone-band"><span class="phone">470-555-0193</span></div>
  </section>

  <!-- 160x600 -->
  <section class="banner skyscraper">
    <p class="headline">We pay cash<br>for houses <span class="accent">in</span><br><span class="accent">any condition</span></p>
    <span class="tag" style="top:139px;width:129px;height:25px;">Probate,</span>
    <span class="tag" style="top:178px;width:138px;height:42px;">Facing for Closure</span>
    <span class="tag" style="top:235px;width:123px;height:64px;">Pass due property taxes</span>
    <span class="tag" style="top:312px;width:134px;height:26px;">and more!</span>
    <div class="photo" role="img" aria-label="Photo of an old weathered wooden farmhouse on a grassy field"></div>
    <svg style="position:absolute;left:0;top:482px" width="150" height="49" viewBox="0 0 150 49"><polygon points="0,14 75,0 150,14 150,49 0,49" fill="#ffffff"/></svg>
    <span class="brand">Brivola</span>
    <div class="phone-band"><span class="phone">470-555-0193</span></div>
  </section>

  <!-- 320x50 set -->
  <section class="banner strip" style="top:196px;">
    <div class="photo" role="img" aria-label="Photo of an old wooden farmhouse"></div>
    <p class="headline">We pay cash for<br>houses <span class="accent">in any condition</span></p>
  </section>
  <section class="banner strip" style="top:263px;">
    <div class="photo" role="img" aria-label="Photo of an old wooden farmhouse"></div>
    <span class="tag" style="left:63px;width:148px;">Probate</span>
  </section>
  <section class="banner strip" style="top:328px;">
    <div class="photo" role="img" aria-label="Photo of an old wooden farmhouse"></div>
    <span class="tag" style="left:50px;width:169px;">Facing for Closure</span>
  </section>
  <section class="banner strip" style="top:396px;">
    <div class="photo" role="img" aria-label="Photo of an old wooden farmhouse"></div>
    <span class="tag" style="left:29px;width:208px;">Pass due property taxes</span>
  </section>
  <div class="strip-logo"><span class="brand">Brivola</span></div>
  <div class="strip-phone"><span class="phone">470-555-0193</span></div>

</body>
</html>
```